【タイトル】
超現実派エンジニアも驚く!
メンタル不調も!恋愛の失敗も!実らない努力も!

全ての原因は56種の「モヤリンk」
最強ワークで過去を手放し、人生を全て好転させよう! 

【書籍の特典情報】
誰でもできる
「セルフ解放ワーク」
の動画プレゼント!

【ターゲット】
引き寄せの法則や成功法則が好きな方向け

【著者】
(元システムエンジニア)
企業サポーター
桐野 沙織

【説明】
電子書籍の表紙のデザインをお願いします。

電子書籍なので、タイトル文字を見やすくしてほしいです。

元システムエンジニアで、企業サポーターという職業柄もあり
とても現実派の私が実感して提供しているワークのお話になります

引き寄せやスピリチュアルとは違うので、
どちらかというと成功の法則のように
現実的なイメージの表紙だと良いかなと思っています。

本文をつけますので参考にしていただければと思います。

見た時に、とてもインパクトがあるように感じました。
電子書籍は、表紙の役割が大きいので
わかりやすさもとても大切だと感じ、選ばせていただきました。

皆様、素敵なデザインをご提案いただきありがとうございます。
とても迷い、投票も行い選択させていただきました。
今後、お仕事やデザインをご依頼させていただく際は
また、よろしくお願いいたします。

```html
<!DOCTYPE html>
<html lang="ja">
<head>
<meta charset="UTF-8">
<title>最強ワークで過去を手放し、人生を全て好転させよう!</title>
<link rel="stylesheet" href="https://fonts.googleapis.com/css2?family=Noto+Sans+JP:wght@500;700;900&display=swap">
<style>
  :root {
    --sky: #7ccdf2;
    --white: #ffffff;
    --ink: #1b1b24;
    --accent: #3a9fd9;
  }
  * { margin: 0; padding: 0; box-sizing: border-box; }
  html, body { width: 749px; height: 1200px; overflow: hidden; }
  body { font-family: "Noto Sans JP", sans-serif; background: var(--sky); }
  .cover { position: relative; width: 749px; height: 1200px; background: var(--sky); }

  .kicker {
    position: absolute; top: 22px; left: 0; width: 100%;
    text-align: center; color: var(--white); font-weight: 900;
    font-size: 50px; letter-spacing: 1px;
  }

  .bubble { position: absolute; left: 88px; top: 98px; width: 560px; height: 180px; }
  .bubble svg { position: absolute; inset: 0; }
  .bubble-text {
    position: absolute; top: 20px; left: 0; width: 560px;
    text-align: center; color: var(--accent); font-weight: 900;
    font-size: 40px; line-height: 1.35;
  }

  .panel {
    position: absolute; left: 45px; top: 270px; width: 662px; height: 868px;
    background: var(--white);
  }
  .panel .line { position: absolute; left: 0; width: 100%; text-align: center; color: var(--ink); font-weight: 900; white-space: nowrap; }
  .cause-1 { top: 14px; font-size: 50px; }
  .cause-2 { top: 82px; font-size: 58px; }
  .work { top: 188px; font-size: 116px; line-height: 1.1; letter-spacing: -2px; }
  .release { top: 342px; font-size: 54px; }
  .life { top: 418px; font-size: 116px; line-height: 1.1; letter-spacing: -2px; }
  .turn { top: 558px; font-size: 82px; line-height: 1.2; letter-spacing: -2px; }
  .wave { position: absolute; left: 0; width: 100%; }

  .author { position: absolute; left: 0; top: 780px; width: 100%; display: flex; justify-content: center; align-items: flex-end; gap: 16px; color: var(--ink); }
  .author-role { font-size: 20px; font-weight: 700; line-height: 1.3; text-align: right; }
  .author-name { font-size: 48px; font-weight: 900; line-height: 1.1; letter-spacing: 2px; }
</style>
</head>
<body>
<main class="cover">
  <p class="kicker">超現実派エンジニアも驚く!</p>

  <div class="bubble">
    <svg width="560" height="180" viewBox="0 0 560 180" aria-hidden="true">
      <path d="M30 0 H530 Q560 0 560 30 V122 Q560 152 530 152 H470 L500 180 L430 152 H30 Q0 152 0 122 V30 Q0 0 30 0 Z" fill="#ffffff"/>
    </svg>
    <p class="bubble-text">メンタル不調も!恋愛の失敗も!<br>実らない努力も!</p>
  </div>

  <section class="panel">
    <h2 class="line cause-1">全ての原因は</h2>
    <h2 class="line cause-2">56種の「モヤリンk」</h2>
    <svg class="wave" style="top:170px" height="12" viewBox="0 0 662 12" aria-hidden="true">
      <line x1="120" y1="6" x2="560" y2="6" stroke="#3a9fd9" stroke-width="4"/>
    </svg>

    <h1 class="line work">最強ワーク</h1>
    <p class="line release">で過去を手放し、</p>
    <svg class="wave" style="top:412px" height="14" viewBox="0 0 662 14" aria-hidden="true">
      <path d="M120 7 q10 -7 20 0 t20 0 t20 0 t20 0 t20 0 t20 0 t20 0 t20 0 t20 0 t20 0 t20 0 t20 0 t20 0 t20 0 t20 0 t20 0 t20 0 t20 0 t20 0 t20 0 t20 0 t20 0" fill="none" stroke="#3a9fd9" stroke-width="3"/>
    </svg>
    <h1 class="line life">人生を全て</h1>
    <h1 class="line turn">好転させよう!</h1>

    <div class="author">
      <p class="author-role">(元システムエンジニア)<br>企業サポーター</p>
      <p class="author-name">桐野沙織</p>
    </div>
  </section>
</main>
</body>
</html>
```